2 Page Simple Modern Flyer for Upholstery Company!

I need a 2 sided printed flyer designed to showcase our company, Tarnwick Upholstery. We specialize in custom Upholstery work on booths, banquettes, chairs, etc for restaurants, bars, cafes, medical clinics, schools, condo towers, etc. I need the flyer to combine a brief description and history of the company, the logo, address & contact info as well as several provided project photos with a title of that job and company. Finally I need to have a some sort of list to show the different clients we have worked with.
Those clients include:
Halvern Arena
The Silver Quarry Casino
Dunmo
Corvello Pizza
PKLU
Juniper Hall
Faithful Teds
Oar & Lantern
Brackley Crossing Mall
Kesterfield Polytechnic
Torvane
And Many more.
This is the brief description of the company needed:
Tarnwick Upholstery has been serving North America for over 60 years. The company began as a family owned and operated business and has grown into a complete manufacturing facility. We can carry your vision straight through the manufacturing process, from initial drawings to finished product, including foam, fabric, framework, and associated millwork. Our 25,000 square foot facility has computer controlled cutters for both fabric and wood cutting capabilities. We have the capacity to take an original design and create products to meet your specifications, or adapt our standardized designs to fit your vision. We have a library of standard configurations that are customizable to meet almost any requirements.
The Contact info that needs to be included:
555-318-6472
www.tarnwickupholstery.example
4182 Mossvale Rd. Edmonton, AB. T9X 7K1
I will include the logo image and the several other photos that I would like to be used. One of the photos (The Silver Quarry Casino) I would like used in a bigger capacity.
I would like the look to be clean, simple and modern, but also incorporate some depth of a perhaps a few different shades of blues, greys, blacks and whites, similar to the logo design. I will attach a few photo examples of design I liked.
Let me know immediately if you have any questions or need any references.
Thanks.
Target Market(s)
Designers, Architects, Builders, Contractors, Business Owners.
Industry/Entity Type
It Company
Font styles to use
Requirements
Must have
- A simple modern design. Possibly using different geometric shapes (traingles, diamonds, squares, rectangles, etc) similar to the examples provided.
- Different Shades of blue, grey and black as the color themes.
- -The provided company description
- -The provided contact info
- -The logo provided
Nice to have
- The logo improved and turned into a separate vector file for future use would be a major plus.
- Some sort of leather looking fabric (grey, dark grey or some shade of blue) as a background to show more of an upholstery look if possible.
- -Use of all 13 provided photos if possible.
- -Logos of all the clients we have worked with.
Should not have
- Too Busy
- Too cluttered

```html
<!DOCTYPE html>
<html lang="en">
<head>
<meta charset="utf-8">
<title>Tarnwick Upholstery Flyer</title>
<link rel="stylesheet" href="https://fonts.googleapis.com/css2?family=Source+Sans+3:wght@400;600&display=swap">
<style>
:root{
  --stage:#bfc0c2;
  --paper:#ffffff;
  --ink:#1d1d1f;
  --text-grey:#3e3f42;
  --blue:#1487c9;
  --blue-deep:#0d5f9a;
  --blue-light:#3aa7e0;
  --night:#111214;
  --night-mid:#34373c;
  --white:#ffffff;
}
*{margin:0;padding:0;box-sizing:border-box}
html,body{width:1200px;height:831px;overflow:hidden}
body{background:var(--stage);font-family:"Source Sans 3",sans-serif;position:relative}
.page{position:absolute;top:77px;width:466px;height:661px;background:var(--paper);overflow:hidden;box-shadow:6px 8px 10px rgba(0,0,0,.35)}
.page--front{left:112px}
.page--back{left:620px}
.photo{position:absolute}
.brand{font-weight:600;text-align:center;line-height:1}
.brand__name{display:block;font-size:54px;letter-spacing:1px}
.brand__tag{display:block;font-size:13px;letter-spacing:5px;margin-top:6px}
/* front */
.front__brand{position:absolute;top:28px;left:0;width:466px;color:var(--ink)}
.front__photo{top:126px;left:0;width:466px;height:270px;background:linear-gradient(160deg,#2c2a22 0%,#6b5330 40%,#b08654 70%,#3c2e22 100%)}
.front__curve{position:absolute;top:0;left:0}
.front__dark{position:absolute;top:394px;left:0;width:466px;height:226px;background:radial-gradient(ellipse at 50% 30%,var(--night-mid),var(--night) 80%)}
.ribbon{position:absolute;top:396px;left:124px;width:228px;height:74px}
.ribbon__text{position:absolute;top:18px;left:0;width:228px;text-align:center;color:var(--white);font-size:14.5px;line-height:21px;font-weight:600}
.front__copy{position:absolute;top:492px;left:29px;width:417px;color:#e6e6e6;font-size:10.5px;line-height:13.6px;text-align:justify}
.front__copy p{margin-bottom:12px}
.front__rule{position:absolute;top:620px;left:0;width:466px;height:3px;background:var(--white)}
.front__bar{position:absolute;top:623px;left:0;width:466px;height:38px;background:linear-gradient(90deg,var(--blue),var(--blue-light) 60%,var(--blue));display:flex;align-items:center;justify-content:center;gap:18px;color:var(--white);font-size:10px}
.contact{display:flex;align-items:center;gap:4px}
.contact svg{flex:none}
/* back */
.back__hero{top:0;left:0;width:466px;height:235px;background:linear-gradient(180deg,#3b2a1e 0%,#7a5a3c 35%,#2f4a5c 70%,#1f2a33 100%)}
.back__thumb{top:240px;height:91px}
.back__thumb--a{left:1px;width:151px;background:linear-gradient(160deg,#dfe4e8,#7d8790)}
.back__thumb--b{left:155px;width:155px;background:linear-gradient(160deg,#f0eeea,#b9a99a)}
.back__thumb--c{left:314px;width:152px;background:linear-gradient(160deg,#b46a3c,#e7e2dc)}
.back__title{position:absolute;top:348px;left:0;width:466px;text-align:center;font-size:14.5px;font-weight:600;color:var(--ink)}
.back__copy{position:absolute;left:26px;width:427px;font-size:10.3px;line-height:13.3px;color:var(--text-grey);text-align:justify}
.back__copy--intro{top:381px}
.back__copy--visit{top:433px}
.clients{position:absolute;top:450px;left:28px;width:420px;list-style:none;display:grid;grid-template-columns:138px 138px 144px;grid-auto-flow:column;grid-template-rows:repeat(4,16.5px);font-size:10.3px;color:var(--text-grey)}
.clients li{display:flex;align-items:center;gap:6px}
.clients li::before{content:"";width:7px;height:7px;border-radius:50%;background:var(--blue);flex:none}
.back__wave{position:absolute;top:519px;left:0}
.back__dark{position:absolute;top:555px;left:0;width:466px;height:94px;background:radial-gradient(ellipse at 40% 40%,var(--night-mid),var(--night) 80%)}
.back__strip{position:absolute;top:649px;left:0;width:466px;height:12px;background:linear-gradient(90deg,var(--blue-deep),var(--blue) 50%,var(--blue-deep))}
.back__brand{position:absolute;top:566px;left:36px;width:170px;color:var(--white)}
.back__brand .brand__name{font-size:44px}
.back__brand .brand__tag{font-size:11px;letter-spacing:4px}
.back__contacts{position:absolute;top:585px;left:236px;list-style:none;color:var(--white);font-size:10px}
.back__contacts li{display:flex;align-items:center;gap:8px;height:20px}
</style>
</head>
<body>

<section class="page page--front">
  <div class="photo front__photo" role="img" aria-label="Photo of a restaurant dining room with tufted leather booths and patterned carpet"></div>
  <svg class="front__curve" width="466" height="180" viewBox="0 0 466 180" aria-hidden="true">
    <path d="M0,0H466V152Q240,108 0,170Z" fill="#1487c9"/>
    <path d="M0,0H466V141Q240,94 0,152Z" fill="#ffffff"/>
  </svg>
  <div class="brand front__brand">
    <span class="brand__name">Tarnwick</span>
    <span class="brand__tag">UPHOLSTERY</span>
  </div>
  <div class="front__dark"></div>
  <div class="ribbon">
    <svg width="228" height="74" viewBox="0 0 228 74" aria-hidden="true">
      <defs><linearGradient id="rib" x1="0" y1="0" x2="0" y2="1"><stop offset="0" stop-color="#1a8fd0"/><stop offset="1" stop-color="#0e6aa8"/></linearGradient></defs>
      <path d="M0,0H228V62Q114,86 0,62Z" fill="url(#rib)"/>
    </svg>
    <div class="ribbon__text">SERVING NORTH AMERICA<br>FOR OVER 60 YEARS.</div>
  </div>
  <div class="front__copy">
    <p>The company began as a family owned and operated business and has grown into a complete manufacturing facility.</p>
    <p>We can carry your vision straight through the manufacturing process, from initial drawings to finished product, including foam, fabric, framework, and associated millwork.</p>
    <p>Our 25,000 square foot facility has computer controlled cutters for both fabric and wood cutting capabilities.</p>
  </div>
  <div class="front__rule"></div>
  <footer class="front__bar">
    <span class="contact"><svg width="9" height="11" viewBox="0 0 9 11"><path d="M4.5,0A4.2,4.2 0 0 0 .3,4.2C.3,7.3 4.5,11 4.5,11S8.7,7.3 8.7,4.2A4.2,4.2 0 0 0 4.5,0ZM4.5,5.8A1.6,1.6 0 1 1 4.5,2.6A1.6,1.6 0 0 1 4.5,5.8Z" fill="#fff"/></svg>4182 Mossvale Rd. Edmonton, AB. T9X 7K1</span>
    <span class="contact"><svg width="11" height="11" viewBox="0 0 11 11"><circle cx="5.5" cy="5.5" r="4.9" fill="none" stroke="#fff"/><path d="M3.6,3.2l1,-.4.7,1.5-.6.5c.3.7.8,1.2 1.5,1.5l.5-.6 1.5.7-.4,1c-2.2,0-4.3-2-4.2-4.2Z" fill="#fff"/></svg>555-318-6472</span>
    <span class="contact"><svg width="10" height="10" viewBox="0 0 10 10"><circle cx="5" cy="5" r="4.4" fill="none" stroke="#fff" stroke-width=".9"/><path d="M.6,5H9.4M5,.6C3,3 3,7 5,9.4M5,.6C7,3 7,7 5,9.4" fill="none" stroke="#fff" stroke-width=".8"/></svg>www.tarnwickupholstery.example</span>
  </footer>
</section>

<section class="page page--back">
  <div class="photo back__hero" role="img" aria-label="Photo of The Silver Quarry Casino restaurant with blue upholstered booths and hanging pendant lights"></div>
  <div class="photo back__thumb back__thumb--a" role="img" aria-label="Photo of a bright lounge with window seating"></div>
  <div class="photo back__thumb back__thumb--b" role="img" aria-label="Photo of a modern food court with upholstered seating"></div>
  <div class="photo back__thumb back__thumb--c" role="img" aria-label="Photo of white upholstered booths in a cafe"></div>
  <h2 class="back__title">Do you want the best?&nbsp; You will get the best!</h2>
  <p class="back__copy back__copy--intro">We have the capacity to take an original design and create products to meet your specifications, or adapt our standardized designs to fit your vision. We have a library of standard configurations that are customizable to meet almost any requirements.</p>
  <p class="back__copy back__copy--visit">Visit some of our customers to see variety and quality products. We’re proud of our work!</p>
  <ul class="clients">
    <li>Halvern Arena</li><li>The Silver Quarry Casino</li><li>Dunmo</li><li>Corvello Pizza</li>
    <li>PKLU</li><li>Juniper Hall</li><li>Faithful Teds</li><li>Oar &amp; Lantern</li>
    <li>Brackley Crossing Mall</li><li>Kesterfield Polytechnic</li><li>Torvane</li><li>And Many more</li>
  </ul>
  <div class="back__dark"></div>
  <svg class="back__wave" width="466" height="45" viewBox="0 0 466 45" aria-hidden="true">
    <path d="M0,14Q230,44 466,20V45H0Z" fill="#141517"/>
    <path d="M0,10Q230,32 466,0V20Q230,44 0,14Z" fill="#1487c9"/>
  </svg>
  <div class="brand back__brand">
    <span class="brand__name">Tarnwick</span>
    <span class="brand__tag">UPHOLSTERY</span>
  </div>
  <ul class="back__contacts">
    <li><svg width="10" height="10" viewBox="0 0 11 11"><circle cx="5.5" cy="5.5" r="4.9" fill="none" stroke="#fff"/><path d="M3.6,3.2l1,-.4.7,1.5-.6.5c.3.7.8,1.2 1.5,1.5l.5-.6 1.5.7-.4,1c-2.2,0-4.3-2-4.2-4.2Z" fill="#fff"/></svg>555-318-6472</li>
    <li><svg width="10" height="10" viewBox="0 0 10 10"><circle cx="5" cy="5" r="4.4" fill="none" stroke="#fff" stroke-width=".9"/><path d="M.6,5H9.4M5,.6C3,3 3,7 5,9.4M5,.6C7,3 7,7 5,9.4" fill="none" stroke="#fff" stroke-width=".8"/></svg>www.tarnwickupholstery.example</li>
    <li><svg width="10" height="12" viewBox="0 0 9 11"><path d="M4.5,0A4.2,4.2 0 0 0 .3,4.2C.3,7.3 4.5,11 4.5,11S8.7,7.3 8.7,4.2A4.2,4.2 0 0 0 4.5,0ZM4.5,5.8A1.6,1.6 0 1 1 4.5,2.6A1.6,1.6 0 0 1 4.5,5.8Z" fill="#fff"/></svg>4182 Mossvale Rd. Edmonton, AB. T9X 7K1</li>
  </ul>
  <div class="back__strip"></div>
</section>

</body>
</html>
```